Stellenanzeige / Anzeigengestaltung für Haustechnikbetrieb
Zielgruppe
Wir sind ein Haustechnikbetrieb. Unsere Schwerpunkte liegen im Bereich Heizungs- Sanitär- u. Klimatechnik, sowie Elektroinstallation für Ein- u. Zweifamilienhäuser.
Ich möchte eine kreative Stellenanzeige, die unsere Vorteile gegenüber den Bewerberfirmen herausstellt.
Aufgabenstellung
Anzeigenschaltung in Printmedien und sozialen Netzwerken
für die Onlineanzeige:
Werbebanner Größe 240x400 Pixel
Bezeichnung(en): Vertical Rectangle, Fat Skyscraper, Vertikales Rechteck
Fläche in Pixel: 96.000
Für Print:
1/4 Seite HOCH 8,4 x 12,6 cm
mögliche Texte:
LUST auf was NEUES? JA!
Das trifft sich gut!
ANLAGENMECHANIKER SHK (M/W) gesucht
o Heimatnaher Arbeitseinsatz oder näheres Umfeld
o 70,00 € Auslöse (bei Übernachung)
o Pünktliche, überdurchschnittliche Bezahlung
o Alle Fahrtstunden werden voll bezahlt
o Dienstwagen
o moderne Werkzeuge, Arbeits- und mobile Endgeräte
o Weihnachtsgeld
o Tankgutscheine
o Zulagen für Hochzeit, Jubiläum (...)
o Weiterbildungsmnaßnahmen und Schulungen
o und vieles mehr...
Alles Weitere erfährst du im persönlichen Gespräch.

```html
<!DOCTYPE html>
<html lang="de">
<head>
<meta charset="utf-8">
<title>Stellenanzeige Anlagenmechaniker SHK</title>
<link href="https://fonts.googleapis.com/css2?family=Montserrat:wght@500;600;700&display=swap" rel="stylesheet">
<style>
  :root{
    --purple:#2a1c74;
    --orange:#ef7d1a;
    --white:#ffffff;
    --stage:#f1efea;
    --photo-light:#c9c6bf;
    --photo-dark:#5d5b55;
    --photo-blue:#3346a6;
  }
  *{margin:0;padding:0;box-sizing:border-box}
  html,body{width:1200px;height:675px;overflow:hidden}
  body{background:var(--stage);font-family:"Montserrat",sans-serif;color:var(--white)}
  .ad{
    position:absolute;left:385px;top:15px;width:430px;height:645px;
    background:var(--purple);overflow:hidden;
    box-shadow:0 4px 10px rgba(0,0,0,.25);
  }
  .ad__visual{position:absolute;left:0;top:0;width:430px;height:240px}
  .ad__band{
    position:absolute;left:0;top:248px;width:430px;height:67px;background:var(--orange);
  }
  .ad__headline{
    position:absolute;left:15px;top:256px;font-size:20px;font-weight:600;line-height:28px;
  }
  .ad__badge{
    position:absolute;left:280px;top:220px;width:124px;height:124px;border-radius:50%;
    background:var(--white);border:4px solid var(--purple);
    display:flex;align-items:center;justify-content:center;
  }
  .ad__brand{font-size:21px;font-weight:700;color:var(--purple);letter-spacing:.5px}
  .ad__title{
    position:absolute;left:13px;top:330px;font-size:18.5px;font-weight:700;line-height:24px;
  }
  .perks{
    position:absolute;top:393px;list-style:none;font-size:10.4px;font-weight:500;
    line-height:13.6px;letter-spacing:-.15px;white-space:nowrap;
  }
  .perks--left{left:12px;width:236px}
  .perks--right{left:253px;width:172px}
  .perks li{position:relative;padding-left:11px}
  .perks--right li{padding-left:8px}
  .perks li::before{
    content:"";position:absolute;left:1px;top:4.5px;width:4.5px;height:4.5px;border-radius:50%;background:var(--white);
  }
  .perks--right li::before{left:0}
  .ad__note{
    position:absolute;left:0;width:100%;top:535px;text-align:center;font-size:13.8px;font-weight:600;
  }
  .ad__contact{
    position:absolute;left:0;width:100%;top:571px;text-align:center;font-size:13.8px;font-weight:600;line-height:19.4px;
  }
</style>
</head>
<body>
  <article class="ad">
    <svg class="ad__visual" viewBox="0 0 430 240" role="img" aria-label="Team in blauer Arbeitskleidung sitzt auf einer Bank über einer Kleinstadt">
      <defs>
        <linearGradient id="photoTone" x1="0" y1="0" x2="0" y2="1">
          <stop offset="0" stop-color="#dcdad4"/>
          <stop offset=".35" stop-color="var(--photo-light)"/>
          <stop offset=".55" stop-color="var(--photo-blue)"/>
          <stop offset=".75" stop-color="var(--photo-dark)"/>
          <stop offset="1" stop-color="#4a4944"/>
        </linearGradient>
      </defs>
      <rect width="430" height="240" fill="url(#photoTone)"/>
      <path d="M0 228 Q230 230 430 164 L430 240 L0 240 Z" fill="var(--purple)"/>
      <path d="M0 227 Q230 229 430 163" fill="none" stroke="var(--white)" stroke-width="2"/>
    </svg>

    <div class="ad__band"></div>
    <h1 class="ad__headline">LUST auf was NEUES?<br>JA! Das trifft sich gut!</h1>

    <div class="ad__badge"><span class="ad__brand">KERBER</span></div>

    <h2 class="ad__title">ANLAGENMECHANIKER<br>SHK (M/W) gesucht</h2>

    <ul class="perks perks--left">
      <li>Heimatnaher Arbeitseinsatz<br>oder näheres Umfeld</li>
      <li>70,00 € Auslöse (bei Übernachung)</li>
      <li>Pünktliche, überdurchschnittliche<br>Bezahlung</li>
      <li>Alle Fahrtstunden werden voll bezahlt</li>
      <li>Dienstwagen</li>
      <li>Moderne Werkzeuge,<br>Arbeits- und mobile Endgeräte</li>
    </ul>
    <ul class="perks perks--right">
      <li>Weihnachtsgeld</li>
      <li>Tankgutscheine</li>
      <li>Zulagen für Hochzeit,<br>Jubiläum (...)</li>
      <li>Weiterbildungsmnaßnahmen<br>sowie Schulungen</li>
      <li>und vieles mehr...</li>
    </ul>

    <p class="ad__note">Alles Weitere erfährst du im persönlichen Gespräch.</p>
    <p class="ad__contact">Wir freuen uns auf deine<br>Bewerbung per E-Mail an Tobias Grünfeld.<br>tobias.gruenfeld@kerber-gmbh.de.</p>
  </article>
</body>
</html>
```